Label Design for American Pet Health Startup

We need your help in creating a line-up of labels for our upcoming products. The products will come in two different sizes/shapes. We have a logo (sourced form ArtSquadron!) to start from and a pretty extensive brief (see attached.) The winning design will be bold, simple, and create a strongly branded look to the whole line while allowing consumers to easily sort through the different SKUs.

The logo and other existing design elements are in the attached powerpoint. I will also post some of the source files.

If you choose to compete for this project, please read the creative brief and the powerpoint very carefully before starting.

Thank you for your time and consideration.

Target Market(s)

Pet owners (dog owners, initially) who care deeply about their pets. Their pets are older and may not be thriving the way they once were. The owners want their pets to have the highest quality of life possible, for as long as is practical. They take their pets frequently to the vet and have great faith in veterinary medicine, but they also believe that dietary supplements may have a beneficial effect. They believe this to be possible because they take supplements themselves.

They are probably older--empty nesters or soon to be. They’ve owned their dog for five years or more, or have rescued an older dog from a shelter. Their dog is, in many ways, a full member of their family.

Industry/Entity Type

Pet Care

Font styles to use
Sans Serif

Requirements
Must have
• Please see the attached brief for this detail. I have cut and paste it into this form but it doesn't translate well. Reading the Word document will be easier and the links will work.
• Packaging Creative Considerations: The product packaging needs to . . .
• • Have a strong, branded line look.
• - The logo has already been developed, and I would like you to be guided in your design choices by its structure and color, but I am open to deviations from the existing work if it leads to a strong design
• • Use color or some other design elements to distinguish each SKU from the other
• • Be bold and simple. This product will typically be merchandised online, with very small images of the packaging. Simple and bold design elements will ensure that the products are both noticed and understood.
• - The product will likely be contained within white plastic or aluminum (silver) bottles with white caps/pumps. However, if you believe your design concepts would benefit from a particular color of bottle/container, please illustrate that, as that would be possible to execute.
• • Communicate that these products are for pets without using any clichés. This category is full of packaging with stock photos of dogs and cats. Please avoid this at all costs. Instead, please unleash your creativity to illustrate the products’ nature/purposes.
• A couple of packaging designs I would like you to draw inspiration from:
• o Vemo. This line is for human supplements/vitamins. Notice the strong line look, the simple and bold graphics, and the smart use of color and other design elements to differentiate the SKUs (while still holding it together as a single brand.)
• o Tupka. This line is for pets. Again, notice the strong line look, the smart use of color to differentiate the SKUs, and the simple and bold presentation that translates so well on the screen.
• o Crumblefin. This design is not as good as the first two, but it does accomplish several of the brief’s objectives and the packaging is likely to be very similar to what your design will eventually be affixed to.
• Design Deliverables: A great submission will illustrate its strength by showing how the design translates across all the expected SKUs. To accomplish, this, I would recommend using the “functional maps” I’ve included in the attached Powerpoint document to:
• o First illustrate, in greater size and detail, one SKU each of the two families (one oil SKU and one supplement SKU)
• o Then illustrate how each of those designs extends across the rest of the family. That illustration can be less detailed. We just need to see how the colors and other design elements extend.
Should not have
• No stock images of cats or dogs; please avoid junking up the designs with too many elements

```html
<!DOCTYPE html>
<html lang="en">
<head>
<meta charset="utf-8">
<title>Tailvane Soft Chew Labels</title>
<link href="https://fonts.googleapis.com/css2?family=Advent+Pro:wght@600;700&family=Titillium+Web:wght@400;600;700&display=swap" rel="stylesheet">
<style>
  :root {
    --canvas: #d5d5d5;
    --paper: #ffffff;
    --brand-teal: #3aa9b8;
    --wordmark: #5c5c5c;
    --immunity: #5b8b1c;
    --immunity-accent: #b6ec2a;
    --digestion: #bfb10b;
    --digestion-accent: #f4ecb0;
    --joint: #3caec0;
    --joint-accent: #d4f2f6;
    --skin: #d2110f;
    --skin-accent: #f7c2b8;
    --multi: #e9540d;
    --multi-accent: #fbd36a;
  }
  * { margin: 0; padding: 0; box-sizing: border-box; }
  html, body { width: 1200px; height: 793px; overflow: hidden; background: var(--canvas); }
  body { position: relative; font-family: "Titillium Web", Arial, sans-serif; }

  .label {
    position: absolute; width: 343px; height: 308px;
    background: var(--paper); overflow: hidden;
  }
  .label--immunity  { left: 45px;  top: 62px;  --sku: var(--immunity);  --accent: var(--immunity-accent); }
  .label--digestion { left: 430px; top: 62px;  --sku: var(--digestion); --accent: var(--digestion-accent); }
  .label--joint     { left: 813px; top: 62px;  --sku: var(--joint);     --accent: var(--joint-accent); }
  .label--skin      { left: 233px; top: 416px; --sku: var(--skin);      --accent: var(--skin-accent); }
  .label--multi     { left: 623px; top: 416px; --sku: var(--multi);     --accent: var(--multi-accent); }

  .brand { position: absolute; left: 0; top: 0; width: 100%; height: 100px; text-align: center; }
  .brand__square {
    position: absolute; left: 149px; top: 12px; width: 45px; height: 45px;
    border-radius: 6px; background: var(--brand-teal);
  }
  .brand__name {
    position: absolute; left: 0; right: 0; top: 60px;
    font-size: 29px; font-weight: 400; color: var(--wordmark); line-height: 1;
  }

  .band {
    position: absolute; left: 0; top: 100px; width: 100%; height: 208px;
    background: var(--sku); color: #fff; text-align: center;
  }
  .band__art {
    position: absolute; inset: 0;
    background: radial-gradient(ellipse 45% 60% at 70% 55%, rgba(0,0,0,0.13), rgba(0,0,0,0) 70%);
  }
  .title {
    position: absolute; left: 0; right: 0; top: 5px;
    font-family: "Advent Pro", Arial, sans-serif; font-weight: 700;
    font-size: 46px; line-height: 1; letter-spacing: 1px; text-transform: uppercase;
  }
  .title small { font-size: 22px; }
  .title__kicker {
    display: block; font-size: 21px; letter-spacing: 1px; margin-bottom: -3px;
  }
  .title--stacked { top: 1px; }
  .title--stacked .title__main { font-size: 48px; display: block; }
  .claim {
    position: absolute; left: 40px; right: 40px; top: 57px;
    font-size: 8.5px; font-weight: 600; line-height: 1.5; color: var(--accent);
  }
  .claim--light { color: #fff; opacity: 0.85; }
  .pill {
    position: absolute; left: 40px; top: 93px; width: 263px; height: 30px;
    border-radius: 15px; background: #fff; color: var(--sku);
    font-size: 15px; font-weight: 600; line-height: 30px;
  }
  .audience {
    position: absolute; left: 0; right: 0; top: 126px;
    font-size: 17px; font-weight: 700; color: var(--accent);
  }
  .count {
    position: absolute; left: 153px; top: 149px; width: 36px; height: 36px;
    border-radius: 50%; background: #fff; color: var(--sku); line-height: 1;
  }
  .count__num { display: block; font-size: 14px; margin-top: 5px; }
  .count__unit { display: block; font-size: 7px; }
  .weight { position: absolute; left: 0; right: 0; top: 191px; font-size: 8.5px; }
  .origin { position: absolute; left: 15px; top: 157px; width: 60px; text-align: left; }
  .origin svg { display: block; margin-left: 5px; }
  .origin__text { display: block; font-size: 8.5px; margin-top: 3px; }
  .free-from { position: absolute; left: 268px; top: 157px; list-style: none; text-align: left; }
  .free-from li { font-size: 10.5px; line-height: 13.5px; }
  .free-from li::before {
    content: ""; display: inline-block; width: 5px; height: 5px; border-radius: 50%;
    background: #fff; margin-right: 4px; vertical-align: 1px;
  }
</style>
</head>
<body>

<svg width="0" height="0" style="position:absolute">
  <defs>
    <symbol id="flag" viewBox="0 0 42 24">
      <rect width="42" height="24" fill="#ffffff"/>
      <g fill="#d0112b">
        <rect y="0" width="42" height="2"/><rect y="4" width="42" height="2"/>
        <rect y="8" width="42" height="2"/><rect y="12" width="42" height="2"/>
        <rect y="16" width="42" height="2"/><rect y="20" width="42" height="2"/>
      </g>
      <rect width="18" height="12" fill="#2a3a8c"/>
    </symbol>
  </defs>
</svg>

<article class="label label--immunity">
  <header class="brand"><span class="brand__square"></span><div class="brand__name">Tailvane</div></header>
  <section class="band">
    <div class="band__art" role="img" aria-label="Large faint germ silhouette illustration"></div>
    <h2 class="title">Immunity</h2>
    <p class="claim">Supports a Healthy Immune System with Vitamin B12,<br>Vitamin C, &amp; Zinc</p>
    <div class="pill">Soft &amp; Chewable Supplements</div>
    <div class="audience">For Dogs</div>
    <div class="origin"><svg width="42" height="24"><use href="#flag"/></svg><span class="origin__text">Made in USA</span></div>
    <div class="count"><span class="count__num">90</span><span class="count__unit">chews</span></div>
    <div class="weight">Net Wt 16 OZ / 453 g</div>
    <ul class="free-from"><li>No Gluten</li><li>No Grain</li><li>No Soy</li></ul>
  </section>
</article>

<article class="label label--digestion">
  <header class="brand"><span class="brand__square"></span><div class="brand__name">Tailvane</div></header>
  <section class="band">
    <div class="band__art" role="img" aria-label="Large faint stomach silhouette illustration"></div>
    <h2 class="title">Digestion</h2>
    <p class="claim claim--light">Supports Healthy Digestion with Enzymes Pre-Biotics,<br>&amp; Pro-Biotics</p>
    <div class="pill">Soft &amp; Chewable Supplements</div>
    <div class="audience">For Dogs</div>
    <div class="origin"><svg width="42" height="24"><use href="#flag"/></svg><span class="origin__text">Made in USA</span></div>
    <div class="count"><span class="count__num">90</span><span class="count__unit">chews</span></div>
    <div class="weight">Net Wt 16 OZ / 453 g</div>
    <ul class="free-from"><li>No Gluten</li><li>No Grain</li><li>No Soy</li></ul>
  </section>
</article>

<article class="label label--joint">
  <header class="brand"><span class="brand__square"></span><div class="brand__name">Tailvane</div></header>
  <section class="band">
    <div class="band__art" role="img" aria-label="Large faint hip joint bone illustration"></div>
    <h2 class="title">Hip <small>&amp;</small> Joint</h2>
    <p class="claim">Supports Healthy Joints with Glucosamine Chondroitin,<br>&amp; Willow Bark</p>
    <div class="pill">Soft &amp; Chewable Supplements</div>
    <div class="audience">For Dogs</div>
    <div class="origin"><svg width="42" height="24"><use href="#flag"/></svg><span class="origin__text">Made in USA</span></div>
    <div class="count"><span class="count__num">90</span><span class="count__unit">chews</span></div>
    <div class="weight">Net Wt 16 OZ / 453 g</div>
    <ul class="free-from"><li>No Gluten</li><li>No Grain</li><li>No Soy</li></ul>
  </section>
</article>

<article class="label label--skin">
  <header class="brand"><span class="brand__square"></span><div class="brand__name">Tailvane</div></header>
  <section class="band">
    <div class="band__art" role="img" aria-label="Large faint furry coat silhouette illustration"></div>
    <h2 class="title">Skin <small>&amp;</small> Coat</h2>
    <p class="claim">Supports a Healthy Skin &amp; Coat with B Vitamins<br>Omega-3, &amp; Biotin</p>
    <div class="pill">Soft &amp; Chewable Supplements</div>
    <div class="audience">For Dogs</div>
    <div class="origin"><svg width="42" height="24"><use href="#flag"/></svg><span class="origin__text">Made in USA</span></div>
    <div class="count"><span class="count__num">90</span><span class="count__unit">chews</span></div>
    <div class="weight">Net Wt 16 OZ / 453 g</div>
    <ul class="free-from"><li>No Gluten</li><li>No Grain</li><li>No Soy</li></ul>
  </section>
</article>

<article class="label label--multi">
  <header class="brand"><span class="brand__square"></span><div class="brand__name">Tailvane</div></header>
  <section class="band">
    <div class="band__art" role="img" aria-label="Large faint circles of vitamin and molecule illustration"></div>
    <h2 class="title title--stacked"><span class="title__kicker">Canine</span><span class="title__main">Multi</span></h2>
    <p class="claim" style="top:69px">A Blend of Vitamins, Minerals<br>&amp; Antioxidants for Daily Health Support</p>
    <div class="pill">Soft &amp; Chewable Supplements</div>
    <div class="audience">For Dogs</div>
    <div class="origin"><svg width="42" height="24"><use href="#flag"/></svg><span class="origin__text">Made in USA</span></div>
    <div class="count"><span class="count__num">90</span><span class="count__unit">chews</span></div>
    <div class="weight">Net Wt 16 OZ / 453 g</div>
    <ul class="free-from"><li>No Gluten</li><li>No Grain</li><li>No Soy</li></ul>
  </section>
</article>

</body>
</html>
```